Organic Sunscreen Business "VelloBloom" Needs Package Design

Our company VelloBloom, manufactures an anti-ageing SPF 15 sunscreen product.

We specialise in the world's most rare and luxury organic anti-ageing ingredients.

We require an attractive package design for a 2.5 oz/75 ml squeezy bottle with box design, a few examples of similar examples which we like are attached.

We have a logo, barcode and graphic, which has been uploaded, and the bottle is to convey the message of wealth and luxury as well as organic sunscreen, we would prefer the package to be colourful and creative in order to sell.

I have included 2 rough sketches of the basic elements and layout of the design. And the box is to be similar to the bottle but to contain an extra caption.

Also, the sketch is only for a guide on how I would like the package, i.e. the labels and graphics can be in different positions/layouts thanks. And any additional creative images, text or fonts would be considered.
Updates

Industry/Entity Type

Business

Requirements
Must have
• FRONT of Bottle:
• LABEL 1: Logo (attached)
• LABEL 2:
• SPF 15
• Non-Nano
• Technology
• 100% Organic
• Paraben Free
• LABEL 3: (Larger/higher emphasis than Label 2)
• Anti-Ageing
• Moisturiser
• BACK of Bottle:
• Introduction: (For me to add personally at later date)
• Warnings: For external use only. Do not use on damaged or broken skin. Stop use and ask a doctor if rash occurs. When using this product keep out of eyes. Rinse with water to remove.
• Directions: Shake well before use. Apply liberally 15 minutes before sun exposure. Use a water resistant sunscreen if swimming or sweating. Reapply at least every 2 hours. Children under 6 months: Ask a doctor.
• Active Ingredient: Non-Nano Zinc Oxide (6%)
• Also contains: (For me to add personally at later date)
• Barcode: (image attached)
• Contact: www.vellobloom-example.com.au
• 2.5oz/7ml e
• BOX:
• Same as bottle, but one side will contain the caption:
• "7 NATURAL WONDERS IN 1" (In a creative style)
Nice to have
• Additional Text/Images/Fonts relating to the subject(s)
• Most creative design will be the winner.

```html
<!DOCTYPE html>
<html lang="en">
<head>
<meta charset="utf-8">
<title>VelloBloom Anti-Ageing Moisturiser Packaging</title>
<link href="https://fonts.googleapis.com/css2?family=Cinzel:wght@400;500&display=swap" rel="stylesheet">
<style>
  :root {
    --stage: #ebebea;
    --kraft: #c8bea9;
    --kraft-light: #d3cab7;
    --kraft-dark: #b9ae97;
    --ink: #3a3733;
    --rule: #4a4640;
    --gold-1: #f6e27a;
    --gold-2: #c99a1e;
    --gold-3: #8d6a12;
    --cap: #2b2a28;
    --cap-edge: #151413;
    --photo-sky: #9a9a9a;
    --photo-sand: #e8e8e6;
  }
  * { margin: 0; padding: 0; box-sizing: border-box; }
  html, body {
    width: 1200px; height: 938px; overflow: hidden;
    background: var(--stage);
    font-family: "Cinzel", serif;
    color: var(--ink);
  }
  .canvas { position: relative; width: 1200px; height: 938px; }

  /* ---------- Box side panel ---------- */
  .box-side {
    position: absolute; left: 190px; top: 100px;
    width: 172px; height: 668px;
    background: var(--kraft-dark);
    display: flex; flex-direction: column; align-items: center; justify-content: center;
  }
  .vine {
    position: absolute; width: 120px; height: 150px;
    background: linear-gradient(135deg, rgba(58,55,51,.35), rgba(58,55,51,0) 75%);
  }
  .vine--top { left: 0; top: 0; }
  .vine--bottom { right: 0; bottom: 0; background: linear-gradient(315deg, rgba(58,55,51,.35), rgba(58,55,51,0) 75%); }
  .wonders {
    text-align: center; font-size: 31px; line-height: 1.45; letter-spacing: .5px;
  }
  .wonders .numeral { display: block; font-size: 56px; line-height: 1.3; }

  /* ---------- Box front panel ---------- */
  .box-front {
    position: absolute; left: 362px; top: 100px;
    width: 188px; height: 668px;
    background: var(--kraft);
    display: flex; flex-direction: column; align-items: center;
  }
  .photo {
    width: 100%;
    background: linear-gradient(180deg, var(--photo-sky) 0%, #c9c9c9 45%, #7d7d7d 55%, var(--photo-sand) 75%, #f4f4f2 100%);
  }
  .box-front .photo { height: 196px; }
  .title { text-align: center; font-weight: 400; line-height: 1.05; }
  .box-front .title { font-size: 27px; margin-top: 14px; }
  .rule { width: 100%; height: 2px; background: var(--rule); }
  .box-front .rule { margin-top: 8px; }
  .claims { text-align: center; }
  .box-front .claims { font-size: 15px; line-height: 1.2; margin-top: 6px; }
  .spf {
    background: linear-gradient(160deg, var(--gold-3), var(--gold-1) 35%, var(--gold-2) 65%, var(--gold-1) 85%, var(--gold-3));
    color: #2c2310; text-align: center;
  }
  .box-front .spf { font-size: 31px; width: 112px; height: 40px; line-height: 40px; margin-top: 12px; }
  .tech { text-align: center; }
  .box-front .tech { font-size: 11px; margin-top: 4px; letter-spacing: .3px; }
  .brand { display: flex; align-items: center; gap: 8px; color: var(--ink); }
  .brand-dot { border-radius: 50%; background: var(--gold-2); }
  .box-front .brand { margin-top: 78px; font-size: 15px; }
  .box-front .brand-dot { width: 12px; height: 12px; }
  .volume { text-align: center; }
  .box-front .volume { margin-top: auto; margin-bottom: 28px; font-size: 14px; }

  /* ---------- Tube ---------- */
  .tube {
    position: absolute; left: 606px; top: 150px;
    width: 348px; height: 560px;
    background: var(--kraft);
    clip-path: polygon(0 0, 100% 0, 89% 100%, 11% 100%);
    display: flex; flex-direction: column; align-items: center;
  }
  .tube .photo { height: 178px; }
  .tube .title { font-size: 26px; margin-top: 22px; letter-spacing: .5px; }
  .tube .rule { width: 86%; margin-top: 8px; }
  .tube .claims { font-size: 13.5px; margin-top: 6px; letter-spacing: .3px; }
  .tube .spf { font-size: 30px; width: 138px; height: 38px; line-height: 38px; margin-top: 22px; }
  .tube .tech { font-size: 13.5px; margin-top: 16px; letter-spacing: .4px; }
  .tube .brand { margin-top: 60px; font-size: 14px; }
  .tube .brand-dot { width: 12px; height: 12px; }
  .tube .volume { margin-top: 24px; font-size: 11.5px; }

  .cap { position: absolute; left: 662px; top: 710px; width: 236px; height: 110px; }
</style>
</head>
<body>
<div class="canvas">

  <section class="box-side">
    <div class="vine vine--top" role="img" aria-label="Floral vine ornament"></div>
    <p class="wonders">7 Natural<br>Wonders<br>in<span class="numeral">1</span></p>
    <div class="vine vine--bottom" role="img" aria-label="Floral vine ornament"></div>
  </section>

  <section class="box-front">
    <div class="photo" role="img" aria-label="Black and white photograph of desert pyramids under a cloudy sky"></div>
    <h1 class="title">Anti-Ageing<br>Moisturiser</h1>
    <div class="rule"></div>
    <p class="claims">100% Organic<br>Paraben Free</p>
    <div class="spf">SPF 15</div>
    <p class="tech">Non-Nano Technology</p>
    <div class="brand"><span class="brand-dot"></span>VelloBloom</div>
    <p class="volume">2.5oz/75ml e</p>
  </section>

  <section class="tube">
    <div class="photo" role="img" aria-label="Black and white photograph of desert pyramids under a cloudy sky"></div>
    <h2 class="title">Anti-Ageing<br>Moisturiser</h2>
    <div class="rule"></div>
    <p class="claims">100% Organic - Paraben Free</p>
    <div class="spf">SPF 15</div>
    <p class="tech">Non-Nano Technology</p>
    <div class="brand"><span class="brand-dot"></span>VelloBloom</div>
    <p class="volume">2.5oz/75ml e</p>
  </section>

  <svg class="cap" viewBox="0 0 236 110" aria-hidden="true">
    <path d="M0 0 H236 V96 Q236 110 222 110 H14 Q0 110 0 96 Z" fill="var(--cap)"/>
    <path d="M78 110 V74 Q78 52 118 52 Q158 52 158 74 V110" fill="none" stroke="var(--cap-edge)" stroke-width="3"/>
  </svg>

</div>
</body>
</html>
```